依頼詳細
オープン前のプレオープンで使用するチラシ依頼です。
キャンペーン価格で5日間限定で初回は初見料と施術代で9000円が500円1日限定で10名

こんなお困りの症状はありませんか?

・整体やマッサージに通っているが、肩がこって仕事や日常生活がつらい
・腰痛で電気をあてたり、整骨院に行っても変化がなく諦めている
・頻繁に頭痛に襲われて辛いので、その度に頭痛薬を飲む
・生理前後に痛みが強く、鎮痛薬を飲んでしまう
・精神薬を処方されたが、いつまで飲み続けるのか不安だけどやめられない
・病院で薬をもらったが一向にめまいが改善しない
の項目はなるべく全部入れたいです。

女性に特化した整体院なのでそこがイメージしやすいデザインがありがたいです。
記載項目
店名:自律神経専門 整体院 ゆらぎ→自律神経専門を目立たせて欲しいです。

URL:https://yuragi-karada.example/

地図→詳細を送りますので作成して頂きたいです。

スタッフ写真もしくは女性が施術している写真を入れて欲しいです。

マンションの外装写真を入れるか目印のマルカワ堂がすぐ近く(ビル1つとなり)なので場所イメージがついたほうがいい気がするのでそこの情報はどちらか入れたいです。
電話番号とラインに関しては7月中に取得します。

院内
・予約優先制
・女性セラピスト指名OK
・施術ルーム完全個室
・キッズスペースあり
・ロゴ
を入れたいです。

サイズ
A4
ページ数
両面
希望イメージ
シンプル 複雑
単色 カラフル
暗い 明るい
日常 高級
遊び心 厳粛
未来的 伝統的
女性的 男性的
希望する色
赤系、緑系、茶系
納品ファイル
• 高解像度JPG (.jpg)
• PNG形式 (.png)
補足説明
可能であれば当社でも内容を修正することができれば助かります。
出来る限りインパクトの強いチラシが希望です。

「自律神経専門」整体院の自律神経専門が目立ちたいです。
宜しくお願い致します。

```html
<!DOCTYPE html>
<html lang="ja">
<head>
<meta charset="utf-8">
<title>自律神経専門 整体院 ゆらぎ 開院チラシ</title>
<link rel="stylesheet" href="https://fonts.googleapis.com/css2?family=M+PLUS+Rounded+1c:wght@500;700;800&family=Noto+Serif+JP:wght@700;900&family=Montserrat:ital,wght@1,800&display=swap">
<style>
  :root{
    --cream:#fbf8f1;
    --brown:#6b4a2f;
    --orange:#f08a1c;
    --orange-deep:#e8631a;
    --green:#3f6b34;
    --green-soft:#9cc46b;
    --leaf-light:#dcebc3;
    --yellow:#ffe45c;
    --row:#fff4e3;
    --white:#ffffff;
  }
  *{margin:0;padding:0;box-sizing:border-box}
  html,body{width:849px;height:1200px;overflow:hidden;background:var(--cream)}
  body{font-family:"M PLUS Rounded 1c",sans-serif;color:var(--brown)}
  .flyer{position:relative;width:849px;height:1200px;overflow:hidden;background:var(--cream)}

  .tagline{position:absolute;top:18px;left:0;width:100%;text-align:center;font-size:22px;font-weight:800;letter-spacing:1px;color:var(--brown);z-index:2}

  .hero-photo{position:absolute;top:56px;left:0;width:849px;height:510px;
    background:linear-gradient(100deg,#f6efe6 0%,#efe3d6 35%,#e9d9c9 60%,#dcc7b5 100%)}
  .hero-fade{position:absolute;top:340px;left:0;width:849px;height:230px;
    background:linear-gradient(180deg,rgba(251,248,241,0) 0%,rgba(251,248,241,.85) 50%,var(--cream) 100%)}
  .leaves-top{position:absolute;top:40px;left:0;width:110px;height:300px;
    background:radial-gradient(ellipse at 0 30%,var(--green-soft) 0%,rgba(156,196,107,0) 70%)}

  .media-badge{position:absolute;top:220px;left:110px;width:110px;height:110px;border-radius:50%;
    background:var(--green);color:var(--white);display:flex;align-items:center;justify-content:center;
    text-align:center;font-weight:800;font-size:18px;line-height:1.3;transform:rotate(-8deg)}

  .clinic-name{position:absolute;top:362px;left:112px;font-size:26px;font-weight:800;color:var(--brown);letter-spacing:1px}
  .open-date{position:absolute;top:408px;left:106px;font-family:"Noto Serif JP",serif;font-weight:900;
    font-size:88px;color:var(--orange);letter-spacing:-1px;line-height:1;white-space:nowrap}
  .open-date .weekday{display:inline-flex;width:50px;height:50px;border-radius:50%;background:var(--orange);
    color:var(--white);font-size:26px;align-items:center;justify-content:center;vertical-align:middle;margin-left:6px}

  .open-line{position:absolute;top:530px;left:112px;display:flex;align-items:center;gap:14px}
  .long-awaited{display:flex;align-items:center;justify-content:center;writing-mode:vertical-rl;
    width:54px;height:120px;border:3px solid var(--orange-deep);color:var(--orange-deep);
    background:var(--white);font-weight:800;font-size:28px;letter-spacing:4px;line-height:1}
  .opening{font-family:"Noto Serif JP",serif;font-weight:900;font-size:120px;color:var(--orange-deep);line-height:1;white-space:nowrap}

  .campaign{position:absolute;top:350px;left:560px;width:280px;height:280px;border-radius:50%;
    background:var(--white);box-shadow:0 4px 14px rgba(107,74,47,.15);text-align:center}
  .campaign .title{position:absolute;top:36px;left:0;width:100%;font-family:"Montserrat",sans-serif;font-style:italic;
    font-weight:800;color:var(--orange);font-size:36px;line-height:1;transform:rotate(-6deg)}
  .campaign .regular{position:absolute;top:116px;left:20px;width:240px;font-size:13px;font-weight:700;color:var(--brown)}
  .campaign .regular s{font-size:16px;margin-left:6px}
  .campaign .limits{position:absolute;top:140px;left:34px;display:flex;gap:6px}
  .campaign .limits span{width:52px;height:52px;border-radius:50%;background:var(--orange);color:var(--white);
    font-size:12px;font-weight:800;display:flex;align-items:center;justify-content:center;line-height:1.2}
  .campaign .price{position:absolute;top:198px;left:28px;font-family:"Montserrat",sans-serif;font-weight:800;
    font-style:italic;font-size:58px;color:var(--orange-deep);line-height:1}
  .campaign .tax{position:absolute;top:208px;left:204px;width:38px;height:38px;border-radius:50%;background:var(--leaf-light);
    color:var(--brown);font-size:12px;font-weight:800;display:flex;align-items:center;justify-content:center}

  .symptoms{position:absolute;top:688px;left:40px;width:584px;height:344px;background:var(--white);
    border:3px solid var(--orange);border-radius:10px;padding:12px 16px}
  .symptoms h2{font-size:22px;font-weight:800;color:var(--brown);margin-bottom:10px;letter-spacing:1px;line-height:1.3}
  .symptoms h2 em{font-style:normal;color:var(--orange-deep)}
  .symptom-list{list-style:none;display:flex;flex-direction:column;gap:6px}
  .symptom-list li{display:flex;align-items:center;gap:8px;background:var(--row);border-radius:6px;
    padding:0 10px;height:40px;font-size:14px;font-weight:700;line-height:1.3;white-space:nowrap}
  .symptom-list svg{flex:none}

  .cause-band{position:absolute;top:1046px;left:0;width:849px;height:62px;background:var(--green);
    color:var(--white);display:flex;align-items:center;justify-content:center;font-size:30px;font-weight:800;letter-spacing:1px}
  .cause-band em{font-style:normal;color:var(--yellow)}
  .promise{position:absolute;top:1122px;left:0;width:100%;text-align:center;font-size:22px;font-weight:800;color:var(--brown);z-index:2}
  .promise em{font-style:normal;color:var(--orange-deep);font-size:26px}
  .leaves-bottom{position:absolute;top:1150px;left:0;width:849px;height:50px;
    background:linear-gradient(180deg,rgba(156,196,107,0) 0%,var(--leaf-light) 45%,var(--green-soft) 100%)}
</style>
</head>
<body>
<div class="flyer">
  <div class="hero-photo" role="img" aria-label="女性セラピストが女性の首元を施術している写真"></div>
  <div class="hero-fade"></div>
  <div class="leaves-top" role="img" aria-label="緑の葉の飾り"></div>

  <p class="tagline">心身両面から「キレイ」を取り戻す、女性専門の自律神経専門整体院</p>

  <div class="media-badge">メディア<br>掲載多数!</div>

  <p class="clinic-name">自律神経専門整体院 ゆらぎ</p>
  <p class="open-date">9月00日<span class="weekday">曜</span></p>
  <div class="open-line">
    <span class="long-awaited">待望の</span>
    <span class="opening">開院!</span>
  </div>

  <div class="campaign">
    <p class="title">OPEN<br>CAMPAIGN</p>
    <p class="regular">初見料 + 施術代<s>¥9,000</s></p>
    <div class="limits">
      <span>5日間<br>限定</span>
      <span>初回<br>限定</span>
      <span>1日<br>10名様</span>
    </div>
    <p class="price">¥500</p>
    <span class="tax">税込</span>
  </div>

  <section class="symptoms">
    <h2>こんな<em>お困りの症状</em>はありませんか?</h2>
    <ul class="symptom-list">
      <li><svg width="22" height="22" viewBox="0 0 24 24"><rect x="1" y="1" width="22" height="22" rx="4" fill="none" stroke="#f08a1c" stroke-width="2"/><path d="M6 12l4 4 8-9" fill="none" stroke="#e8631a" stroke-width="3" stroke-linecap="round"/></svg>整体やマッサージに通っているが、肩がこって仕事や日常生活がつらい</li>
      <li><svg width="22" height="22" viewBox="0 0 24 24"><rect x="1" y="1" width="22" height="22" rx="4" fill="none" stroke="#f08a1c" stroke-width="2"/><path d="M6 12l4 4 8-9" fill="none" stroke="#e8631a" stroke-width="3" stroke-linecap="round"/></svg>腰痛で電気をあてたり、整骨院に行っても変化がなく諦めている</li>
      <li><svg width="22" height="22" viewBox="0 0 24 24"><rect x="1" y="1" width="22" height="22" rx="4" fill="none" stroke="#f08a1c" stroke-width="2"/><path d="M6 12l4 4 8-9" fill="none" stroke="#e8631a" stroke-width="3" stroke-linecap="round"/></svg>頻繁に頭痛に襲われて辛いので、その度に頭痛薬を飲む</li>
      <li><svg width="22" height="22" viewBox="0 0 24 24"><rect x="1" y="1" width="22" height="22" rx="4" fill="none" stroke="#f08a1c" stroke-width="2"/><path d="M6 12l4 4 8-9" fill="none" stroke="#e8631a" stroke-width="3" stroke-linecap="round"/></svg>生理前後に痛みが強く、鎮痛薬を飲んでしまう</li>
      <li><svg width="22" height="22" viewBox="0 0 24 24"><rect x="1" y="1" width="22" height="22" rx="4" fill="none" stroke="#f08a1c" stroke-width="2"/><path d="M6 12l4 4 8-9" fill="none" stroke="#e8631a" stroke-width="3" stroke-linecap="round"/></svg>精神薬を処方されたが、いつまで飲み続けるのか不安だけどやめられない</li>
      <li><svg width="22" height="22" viewBox="0 0 24 24"><rect x="1" y="1" width="22" height="22" rx="4" fill="none" stroke="#f08a1c" stroke-width="2"/><path d="M6 12l4 4 8-9" fill="none" stroke="#e8631a" stroke-width="3" stroke-linecap="round"/></svg>病院で薬をもらったが一向にめまいが改善しない</li>
    </ul>
  </section>

  <div class="cause-band"><p>それ、全部<em>「自律神経の乱れ」</em>からくる不調です</p></div>
  <p class="promise">当院ならこれらのお悩みをすべて<em>「終わらせる」</em>ことができます</p>

  <div class="leaves-bottom" role="img" aria-label="緑の葉の飾り"></div>
</div>
</body>
</html>
```